Luxury Brand Real Estate For Sale sign

**Update** I've added some examples from the internet of other signs that have a look similar to what I would like to see. I do not want my personal name in the sign. And the word FOR SALE Does not need to be so large - it can be more subtle.
I want to create a Real Estate for sale sign for my company that will be used for luxury/higher end real estate listings. I’m sharing my business card as well as a logo with new teal color to show what we're moving towards: we’re using Teal, white, black and gold.
Hoping the sign is simple, sophisticated and eye catching.
The sign should be 24" wide by 30" tall including the company name: Harbor Crest Realty Group and our logo, office phone number 727-555-0148 and website www.hcrgexample.com the words "For Sale"
Optional to add this e-mail address info@hcrgexample.com to the sign
Target Market(s)
Luxury home buyers
Industry/Entity Type
Real Estate
Look and feel

```html
<!DOCTYPE html>
<html lang="en">
<head>
<meta charset="UTF-8">
<title>Harbor Crest Realty Group – For Sale Sign</title>
<link rel="stylesheet" href="https://fonts.googleapis.com/css2?family=Montserrat:wght@300;400;500;600;700&display=swap">
<style>
  :root {
    --sign-black: #231f20;
    --sign-white: #ffffff;
    --brand-gold: #d9a21f;
    --ink-black: #111111;
    --page-bg: #ffffff;
    --sign-edge: rgba(0, 0, 0, 0.12);
    --sign-shadow: rgba(0, 0, 0, 0.45);
  }
  * { margin: 0; padding: 0; box-sizing: border-box; }
  html, body {
    width: 1200px;
    height: 1000px;
    overflow: hidden;
    background: var(--page-bg);
    font-family: "Montserrat", Arial, sans-serif;
  }
  .sign {
    position: absolute;
    left: 306px;
    top: 133px;
    width: 588px;
    height: 734px;
    background: var(--sign-black);
    box-shadow: 0 0 0 1px var(--sign-edge), 10px 12px 16px -4px var(--sign-shadow);
    overflow: hidden;
  }
  .sign__headline {
    position: absolute;
    left: 62px;
    top: 40px;
    color: var(--sign-white);
    font-weight: 700;
    font-size: 116px;
    line-height: 104px;
    letter-spacing: -1px;
  }
  .sign__rule {
    position: absolute;
    left: 60px;
    top: 285px;
    width: 167px;
    height: 11px;
    background: var(--brand-gold);
  }
  .sign__phone {
    position: absolute;
    left: 58px;
    top: 322px;
    color: var(--sign-white);
    font-weight: 600;
    font-size: 48px;
    line-height: 56px;
    letter-spacing: -1.5px;
  }
  .sign__email {
    position: absolute;
    left: 60px;
    top: 380px;
    color: var(--sign-white);
    font-weight: 500;
    font-size: 25px;
    line-height: 32px;
  }
  .brand-band {
    position: absolute;
    left: 0;
    top: 465px;
    width: 588px;
    height: 185px;
    background: var(--sign-white);
  }
  .brand-band__mark {
    position: absolute;
    left: 58px;
    top: 63px;
    width: 120px;
    height: 61px;
  }
  .brand-band__divider {
    position: absolute;
    left: 200px;
    top: 14px;
    width: 2px;
    height: 160px;
    background: var(--ink-black);
  }
  .brand-band__name {
    position: absolute;
    left: 225px;
    top: 70px;
    color: var(--brand-gold);
    font-weight: 300;
    font-size: 25px;
    line-height: 30px;
    letter-spacing: 0.5px;
    text-transform: uppercase;
  }
  .web-band {
    position: absolute;
    left: 0;
    top: 650px;
    width: 588px;
    height: 84px;
    display: flex;
    align-items: center;
    padding-left: 60px;
  }
  .web-band__url {
    color: var(--brand-gold);
    font-weight: 700;
    font-size: 36px;
    line-height: 1;
    white-space: nowrap;
  }
</style>
</head>
<body>
  <div class="sign">
    <h1 class="sign__headline">FOR<br>SALE</h1>
    <div class="sign__rule"></div>
    <p class="sign__phone">727-555-0148</p>
    <p class="sign__email">info@hcrgexample.com</p>

    <div class="brand-band">
      <svg class="brand-band__mark" viewBox="0 0 120 61" aria-hidden="true">
        <rect x="1.5" y="1.5" width="117" height="58" fill="none" stroke="var(--brand-gold)" stroke-width="3"/>
      </svg>
      <div class="brand-band__divider"></div>
      <p class="brand-band__name">Harbor Crest<br>Realty Group</p>
    </div>

    <div class="web-band">
      <p class="web-band__url">www.hcrgexample.com</p>
    </div>
  </div>
</body>
</html>
```